I am a home builder and developer

I would like some sort of architectural design like a pencil type of drawing of a house but want it to be professional looking and two sided.

Simply I am a custom home builder and land developer. I would like a new design other than what I have now that's what I thought y'all did. I like mostly black maybe with an pencil type of drawing of a house. Like an architectural look.

Industry/Entity Type

Home Builder

```html
<!DOCTYPE html>
<html lang="en">
<head>
<meta charset="utf-8">
<title>Harrow Estate – Business Card</title>
<link href="https://fonts.googleapis.com/css2?family=Lato:wght@300;400;700&display=swap" rel="stylesheet">
<style>
  :root {
    --ink: #231f20;
    --blue: #0a84d6;
    --paper: #ffffff;
    --stage: #e8e9eb;
    --sketch-light: #f2f2f2;
    --sketch-mid: #b9bcc0;
    --photo-light: #e3e5e8;
    --photo-dark: #8f8aa0;
  }
  * { margin: 0; padding: 0; box-sizing: border-box; }
  html, body { width: 1200px; height: 1200px; overflow: hidden; background: var(--stage); font-family: "Lato", sans-serif; }
  .card {
    position: absolute; left: 120px; width: 960px; height: 549px;
    background: var(--paper); overflow: hidden;
    box-shadow: 0 10px 30px rgba(0,0,0,.15);
  }
  .card--front { top: 26px; }
  .card--back { top: 625px; }
  .card svg.art { position: absolute; inset: 0; width: 100%; height: 100%; }

  .brand {
    position: absolute; color: var(--ink);
    font-weight: 400; letter-spacing: 2px; line-height: 1.15; white-space: nowrap;
  }
  .card--front .brand { left: 520px; top: 228px; font-size: 38px; }
  .card--back .brand { left: 112px; top: 46px; font-size: 34px; }

  .agent { position: absolute; left: 112px; top: 140px; color: var(--ink); white-space: nowrap; }
  .agent__name { font-size: 30px; font-weight: 700; letter-spacing: 1px; }
  .agent__name span { font-weight: 300; }
  .agent__role { color: var(--blue); font-size: 14px; letter-spacing: 2px; margin-top: 4px; }

  .contact { position: absolute; left: 112px; color: var(--ink); font-size: 20px; line-height: 1.4; white-space: nowrap; }
  .contact--phone { top: 232px; }
  .contact--web { top: 318px; }
  .address { position: absolute; left: 112px; top: 448px; color: var(--paper); font-size: 20px; line-height: 1.4; white-space: nowrap; }
</style>
</head>
<body>

<section class="card card--front">
  <svg class="art" viewBox="0 0 960 549">
    <defs>
      <linearGradient id="sketchTone" x1="0" y1="0" x2="1" y2="1">
        <stop offset="0" stop-color="var(--sketch-light)"/>
        <stop offset="1" stop-color="var(--sketch-mid)"/>
      </linearGradient>
    </defs>
    <polygon points="0,0 300,0 0,330" fill="var(--ink)"/>
    <polygon points="0,549 0,250 340,549" fill="var(--blue)"/>
    <rect x="150" y="90" width="300" height="300" fill="none" stroke="var(--blue)" stroke-width="18"/>
    <rect x="120" y="120" width="300" height="300" fill="url(#sketchTone)" stroke="var(--paper)" stroke-width="8" role="img" aria-label="Pencil architectural drawing of a house"/>
  </svg>
  <div class="brand">HARROW ESTATE<br>SOLUTIONS</div>
</section>

<section class="card card--back">
  <svg class="art" viewBox="0 0 960 549">
    <defs>
      <linearGradient id="photoTone" x1="0" y1="0" x2="1" y2="1">
        <stop offset="0" stop-color="var(--photo-light)"/>
        <stop offset="1" stop-color="var(--photo-dark)"/>
      </linearGradient>
    </defs>
    <polygon points="0,420 570,420 530,549 0,549" fill="var(--ink)"/>
    <polygon points="690,60 960,60 960,549 640,549" fill="var(--ink)"/>
    <rect x="705" y="110" width="230" height="330" fill="var(--blue)"/>
    <rect x="723" y="128" width="194" height="294" fill="url(#photoTone)" stroke="var(--paper)" stroke-width="6" role="img" aria-label="Photo of a house model on architectural plans"/>
    <g class="icon icon--person">
      <circle cx="68" cy="160" r="17" fill="none" stroke="var(--blue)" stroke-width="2.5"/>
      <circle cx="68" cy="155" r="5" fill="var(--blue)"/>
      <path d="M59 169 q9 -10 18 0" fill="var(--blue)"/>
    </g>
    <g class="icon icon--phone">
      <circle cx="68" cy="252" r="17" fill="none" stroke="var(--blue)" stroke-width="2.5"/>
      <path d="M61 245 q0 14 14 14 l2 -4 -4 -3 -2 2 q-5 -2 -7 -7 l2 -2 -3 -4z" fill="var(--blue)"/>
    </g>
    <g class="icon icon--globe">
      <circle cx="68" cy="338" r="17" fill="none" stroke="var(--blue)" stroke-width="2.5"/>
      <circle cx="68" cy="338" r="9" fill="none" stroke="var(--blue)" stroke-width="2"/>
      <line x1="59" y1="338" x2="77" y2="338" stroke="var(--blue)" stroke-width="2"/>
      <line x1="68" y1="329" x2="68" y2="347" stroke="var(--blue)" stroke-width="2"/>
    </g>
    <g class="icon icon--pin">
      <circle cx="68" cy="468" r="17" fill="none" stroke="var(--blue)" stroke-width="2.5"/>
      <path d="M68 478 l-7 -10 a8 8 0 1 1 14 0z" fill="var(--blue)"/>
      <circle cx="68" cy="464" r="3" fill="var(--ink)"/>
    </g>
  </svg>
  <div class="brand">HARROW ESTATE SOLUTIONS</div>
  <div class="agent">
    <div class="agent__name">DANIEL <span>REEVE</span></div>
    <div class="agent__role">REAL ESTATE AGENT</div>
  </div>
  <div class="contact contact--phone">014 . 552 . 3190<br>014 . 552 . 3191</div>
  <div class="contact contact--web">hello@harrowestate.com<br>www.harrowestate.com</div>
  <div class="address">Cedar Point Plaza East<br>Ohio 40217 - United States</div>
</section>

</body>
</html>
```